modern real estate design
business card/letterhead/envelop
Dorian Parks
President
408 W Birch Avenue Belle Plaine, MN 56093
dorian@tidewaterhomesgroup.com
www.tidewaterhomesgroup.com
Licensed Realtor with Quiet Harbor Real Estate
Escape Gravity.
newell343 newell343
I am also interested in getting a design done for metal business cards. It would be cool to have them die cut, etched, and have our two color logo on them. Thanks.

```html
<!DOCTYPE html>
<html lang="en">
<head>
<meta charset="utf-8">
<title>Tidewater Homes Group – Business Card</title>
<link href="https://fonts.googleapis.com/css2?family=Open+Sans:wght@400;600;700&display=swap" rel="stylesheet">
<style>
  :root {
    --page: #eceeef;
    --card: #ffffff;
    --teal: #2bbfca;
    --navy: #2a5a9c;
    --slate: #5d6166;
    --grey-band: #a7a9ac;
    --grey-light: #d4d6d8;
  }
  * { box-sizing: border-box; margin: 0; padding: 0; }
  html, body { width: 1200px; height: 939px; overflow: hidden; }
  body {
    background: var(--page);
    font-family: "Open Sans", Arial, sans-serif;
    position: relative;
  }
  .card {
    position: absolute;
    top: 321px;
    width: 520px;
    height: 297px;
    background: var(--card);
    box-shadow: 0 6px 18px rgba(0,0,0,0.12);
    overflow: hidden;
  }
  .card--back { left: 60px; }
  .card--front { left: 620px; }

  .card__swoosh { position: absolute; inset: 0; width: 100%; height: 100%; }

  .brand {
    display: flex;
    align-items: center;
    gap: 10px;
  }
  .brand__dot {
    border-radius: 50%;
    background: var(--grey-light);
    flex: none;
  }
  .brand__name {
    font-weight: 700;
    color: var(--slate);
    text-transform: uppercase;
    letter-spacing: 0.08em;
    line-height: 1.15;
  }

  .card--front .brand {
    position: absolute;
    left: 110px;
    top: 112px;
  }
  .card--front .brand__dot { width: 64px; height: 64px; }
  .card--front .brand__name { font-size: 22px; }

  .card--back .brand {
    position: absolute;
    left: 28px;
    top: 28px;
  }
  .card--back .brand__dot { width: 26px; height: 26px; }
  .card--back .brand__name { font-size: 10px; }

  .contact {
    position: absolute;
    left: 28px;
    top: 92px;
  }
  .contact__name {
    font-size: 17px;
    font-weight: 600;
    color: var(--navy);
  }
  .contact__role {
    font-size: 12px;
    color: var(--slate);
    margin-bottom: 8px;
  }
  .contact__list { list-style: none; }
  .contact__item {
    display: flex;
    align-items: center;
    gap: 6px;
    font-size: 9.5px;
    color: var(--slate);
    line-height: 16px;
  }
  .contact__icon { width: 9px; height: 9px; fill: var(--navy); flex: none; }
</style>
</head>
<body>

  <section class="card card--back" aria-label="Business card, contact side">
    <svg class="card__swoosh" viewBox="0 0 520 297" preserveAspectRatio="none" aria-hidden="true">
      <path d="M520 0 L405 0 C470 70 470 200 330 297 L520 297 Z" fill="var(--grey-band)"/>
      <path d="M150 297 C290 285 380 245 440 150 C430 230 380 280 330 297 Z" fill="var(--teal)"/>
    </svg>

    <div class="brand">
      <span class="brand__dot"></span>
      <span class="brand__name">Tidewater<br>Homes Group</span>
    </div>

    <div class="contact">
      <p class="contact__name">Dorian Parks</p>
      <p class="contact__role">Consultant</p>
      <ul class="contact__list">
        <li class="contact__item">
          <svg class="contact__icon" viewBox="0 0 10 10"><path d="M5 0C3 0 1.5 1.5 1.5 3.4 1.5 6 5 10 5 10s3.5-4 3.5-6.6C8.5 1.5 7 0 5 0zm0 4.8a1.4 1.4 0 1 1 0-2.8 1.4 1.4 0 0 1 0 2.8z"/></svg>
          408 W Birch Avenue, Belle Plaine, MN 56093
        </li>
        <li class="contact__item">
          <svg class="contact__icon" viewBox="0 0 10 10"><path d="M2 0.5l2 2.2-1 1.2c.6 1.3 1.6 2.3 2.9 2.9l1.2-1 2.2 2-1 1.7C4.5 9.4.6 5.5.4 1.5z"/></svg>
          T. 555 014 2231
        </li>
        <li class="contact__item">
          <svg class="contact__icon" viewBox="0 0 10 10"><rect x="0.5" y="2" width="9" height="6.5" rx="1"/></svg>
          dorian@tidewaterhomesgroup.com
        </li>
        <li class="contact__item">
          <svg class="contact__icon" viewBox="0 0 10 10"><path d="M2 0.5l2 2.2-1 1.2c.6 1.3 1.6 2.3 2.9 2.9l1.2-1 2.2 2-1 1.7C4.5 9.4.6 5.5.4 1.5z"/></svg>
          M. 555 014 2232
        </li>
        <li class="contact__item">
          <svg class="contact__icon" viewBox="0 0 10 10"><circle cx="5" cy="5" r="4.5"/></svg>
          www.tidewaterhomesgroup.com
        </li>
      </ul>
    </div>
  </section>

  <section class="card card--front" aria-label="Business card, brand side">
    <div class="brand">
      <span class="brand__dot"></span>
      <span class="brand__name">Tidewater<br>Homes Group</span>
    </div>
  </section>

</body>
</html>
```